Coralbend Pastoral Traders Business Cards

We require business cards revamped with our logo. A few details we would like to use.

1. Round Edges
2. Our logo over the top of a wagyu cattle background photo on one side of the card

Other side of the card has the below details.

1. Person Name (First & Last)
2. Job Position
3. Mobile Number
4. Email Address
5. Website Address

Simple & Neat.

Target Market(s)

Sales

Industry/Entity Type

Agriculture

Contact Information for Business Card

CORALBEND PASTORAL TRADERS

Colors

Designer to choose colors to be used in the design.

Requirements
Must have
• Company Logo

```html
<!DOCTYPE html>
<html lang="en">
<head>
<meta charset="utf-8">
<title>Coralbend Pastoral Traders – Business Cards</title>
<link rel="stylesheet" href="https://fonts.googleapis.com/css2?family=Libre+Baskerville:wght@700&family=Montserrat:wght@400;500&display=swap">
<style>
  :root {
    --page-bg: #e6e6e4;
    --maroon: #7a1a2c;
    --ink-grey: #555a60;
    --card-white: #ffffff;
    --pasture-light: #6fae3a;
    --pasture-dark: #3f7a22;
    --hide-brown: #b5642a;
    --faint-mark: #f1e9ea;
  }
  * { margin: 0; padding: 0; box-sizing: border-box; }
  html, body {
    width: 1200px;
    height: 900px;
    overflow: hidden;
    background: var(--page-bg);
  }
  .sheet {
    position: relative;
    width: 1200px;
    height: 900px;
  }
  .card {
    position: absolute;
    left: 270px;
    width: 660px;
    height: 377px;
    border-radius: 30px;
    overflow: hidden;
    box-shadow: 0 10px 28px rgba(0,0,0,0.22);
  }
  .card--front { top: 55px; }
  .card--back  { top: 468px; background: var(--card-white); }

  .front-photo {
    position: absolute;
    inset: 0;
    background:
      radial-gradient(ellipse 40% 45% at 58% 48%, var(--hide-brown) 0%, rgba(181,100,42,0.85) 55%, rgba(181,100,42,0) 100%),
      linear-gradient(170deg, var(--pasture-dark) 0%, var(--pasture-light) 45%, #5d9c2f 100%);
  }
  .front-brand {
    position: absolute;
    left: 40px;
    top: 118px;
    display: flex;
    align-items: center;
    gap: 12px;
  }
  .brand-dot {
    width: 16px;
    height: 16px;
    border-radius: 50%;
    background: currentColor;
    flex: none;
  }
  .brand-name {
    font-family: "Libre Baskerville", serif;
    font-weight: 700;
    font-size: 24px;
    letter-spacing: 1px;
    line-height: 1.15;
  }
  .front-brand { color: #ffffff; }

  .back-mark {
    position: absolute;
    right: -60px;
    top: 80px;
    width: 340px;
    height: 340px;
    border-radius: 50%;
    border: 26px solid var(--faint-mark);
  }
  .back-brand {
    position: absolute;
    left: 0;
    right: 0;
    top: 62px;
    display: flex;
    justify-content: center;
    align-items: center;
    gap: 12px;
    color: var(--maroon);
  }
  .back-brand .brand-name { font-size: 26px; }

  .contact {
    position: absolute;
    left: 56px;
    bottom: 40px;
    font-family: "Montserrat", sans-serif;
    color: var(--ink-grey);
  }
  .contact__name {
    font-family: "Libre Baskerville", serif;
    font-weight: 700;
    font-size: 19px;
    color: var(--maroon);
    letter-spacing: 0.5px;
  }
  .contact__role {
    font-size: 16px;
    margin-top: 2px;
    margin-bottom: 18px;
  }
  .contact__list { list-style: none; }
  .contact__item {
    display: flex;
    align-items: center;
    gap: 12px;
    font-size: 17px;
    line-height: 1.6;
  }
  .contact__icon {
    width: 17px;
    height: 17px;
    flex: none;
  }
</style>
</head>
<body>
<main class="sheet">

  <section class="card card--front">
    <div class="front-photo" role="img" aria-label="Photo of a brown wagyu cow standing on green pasture"></div>
    <div class="front-brand">
      <span class="brand-dot"></span>
      <span class="brand-name">CORALBEND PASTORAL TRADERS</span>
    </div>
  </section>

  <section class="card card--back">
    <div class="back-mark" aria-hidden="true"></div>
    <div class="back-brand">
      <span class="brand-dot"></span>
      <span class="brand-name">CORALBEND PASTORAL TRADERS</span>
    </div>

    <div class="contact">
      <p class="contact__name">DANIEL HARTLEY</p>
      <p class="contact__role">Director</p>
      <ul class="contact__list">
        <li class="contact__item">
          <svg class="contact__icon" viewBox="0 0 24 24" aria-hidden="true">
            <rect x="6" y="2" width="12" height="20" rx="2" fill="none" stroke="var(--maroon)" stroke-width="2"/>
            <line x1="10" y1="18" x2="14" y2="18" stroke="var(--maroon)" stroke-width="2"/>
          </svg>
          <span>369-555-0147</span>
        </li>
        <li class="contact__item">
          <svg class="contact__icon" viewBox="0 0 24 24" aria-hidden="true">
            <rect x="2" y="5" width="20" height="14" fill="var(--maroon)"/>
            <polyline points="2,5 12,13 22,5" fill="none" stroke="#fff" stroke-width="1.6"/>
          </svg>
          <span>info@coralbendpastoral.com</span>
        </li>
        <li class="contact__item">
          <svg class="contact__icon" viewBox="0 0 24 24" aria-hidden="true">
            <circle cx="12" cy="12" r="9.5" fill="none" stroke="var(--maroon)" stroke-width="2"/>
            <ellipse cx="12" cy="12" rx="4.5" ry="9.5" fill="none" stroke="var(--maroon)" stroke-width="1.6"/>
            <line x1="2.5" y1="12" x2="21.5" y2="12" stroke="var(--maroon)" stroke-width="1.6"/>
          </svg>
          <span>www.coralbendpastoral.com</span>
        </li>
      </ul>
    </div>
  </section>

</main>
</body>
</html>
```